Box Truck Wrap design with images and our logo

We need a design for the side of our box truck. We are an HVAC and Plumbing Company serving commercial and residential markets and want something catchy, not too busy but more than just logos. Maybe some equipment and/or verbiage of what we do. Real images would be a bonus. We want people to recognize our brand, see our story on the side of this tuck, much like a billboard, and be motivated to contact us for service.

Target Market(s)

Residential homeowners who need HVAC and Plumbing Services

Industry/Entity Type

Commercial and Residential HVAC

Font styles to use
Other font styles liked:
• Calibri

Colors
0054AA
0677BA
7BADD7
CADEEF
E8F1F8

Requirements
Must have
• Our logo, visible interpretation of what we do - Here is our website - www.quillfordpipeworks.example
Nice to have
• Integrated, easy design
Should not have
• Must not be too busy

```html
<!DOCTYPE html>
<html lang="en">
<head>
<meta charset="utf-8">
<title>Quillford Plumbing Heating &amp; Air Conditioning – Truck Wrap</title>
<link rel="stylesheet" href="https://fonts.googleapis.com/css2?family=Montserrat:wght@500;600;700;800&family=Roboto+Condensed:wght@600&display=swap">
<style>
  :root {
    --brand-blue: #2b4c9f;
    --brand-blue-deep: #213d86;
    --swoosh-black: #141414;
    --panel-white: #eeeff1;
    --page-bg: #ffffff;
    --text-white: #ffffff;
    --rule-grey: #d6d8dc;
  }
  * { margin: 0; padding: 0; box-sizing: border-box; }
  html, body { width: 1200px; height: 1200px; overflow: hidden; background: var(--page-bg); }
  .canvas { position: relative; width: 1200px; height: 1200px; }
  .wrap-side { position: absolute; left: 50px; top: 60px; width: 1100px; height: 520px; }
  .wrap-view { position: absolute; top: 700px; width: 340px; height: 420px; }
  .wrap-view--front-logo { left: 30px; }
  .wrap-view--front-contact { left: 430px; }
  .wrap-view--rear { left: 830px; }
  svg { display: block; }
  .brand-name { font-family: "Montserrat", sans-serif; font-weight: 800; fill: var(--brand-blue); }
  .brand-tagline { font-family: "Montserrat", sans-serif; font-weight: 700; fill: var(--swoosh-black); }
  .service-line { font-family: "Roboto Condensed", sans-serif; font-weight: 600; fill: var(--text-white); letter-spacing: 0.5px; }
  .phone { font-family: "Montserrat", sans-serif; font-weight: 600; fill: var(--brand-blue-deep); }
  .website { font-family: "Montserrat", sans-serif; font-weight: 500; fill: #333; }
  .panel-white { fill: var(--panel-white); }
  .panel-blue { fill: var(--brand-blue); }
  .swoosh { fill: var(--swoosh-black); }
  .social-dot { fill: var(--text-white); }
  .brand-dot { fill: var(--brand-blue); }
</style>
</head>
<body>
<main class="canvas">

  <!-- Side wrap: box body + cab door -->
  <svg class="wrap-side" viewBox="0 0 1100 520" aria-label="Truck side wrap">
    <g class="box-body">
      <rect class="panel-white" x="0" y="0" width="780" height="520" rx="6"/>
      <path class="swoosh" d="M0 275 Q390 340 780 260 L780 278 Q390 362 0 300 Z"/>
      <path class="panel-blue" d="M0 300 Q390 362 780 278 L780 514 Q780 520 774 520 L6 520 Q0 520 0 514 Z"/>

      <circle class="brand-dot" cx="78" cy="200" r="26"/>
      <text class="brand-name" x="40" y="150" font-size="118" textLength="690" lengthAdjust="spacingAndGlyphs">Quillford</text>
      <text class="brand-tagline" x="730" y="210" font-size="34" text-anchor="end">PLUMBING HEATING</text>
      <text class="brand-tagline" x="730" y="250" font-size="34" text-anchor="end">&amp; AIR CONDITIONING</text>

      <text class="service-line" x="40" y="380" font-size="14" textLength="700" lengthAdjust="spacingAndGlyphs">RESIDENTIAL AIR CONDITIONING • RESIDENTIAL HEATING • INDOOR AIR QUALITY • RESIDENTIAL PLUMBING</text>
      <text class="service-line" x="50" y="403" font-size="14" textLength="680" lengthAdjust="spacingAndGlyphs">COMMERCIAL AIR CONDITIONING • COMMERCIAL HEATING • COMMERCIAL PLUMBING • GARAGE HEATERS</text>

      <g class="social-row">
        <circle class="social-dot" cx="626" cy="468" r="10"/>
        <circle class="social-dot" cx="654" cy="468" r="10"/>
        <circle class="social-dot" cx="682" cy="468" r="10"/>
        <circle class="social-dot" cx="710" cy="468" r="10"/>
      </g>
    </g>

    <g class="cab-door">
      <rect class="panel-white" x="800" y="160" width="300" height="360" rx="10"/>
      <text class="phone" x="950" y="310" font-size="30" text-anchor="middle">(555) 014-7720</text>
      <text class="website" x="950" y="338" font-size="14" text-anchor="middle">www.quillfordpipeworks.example</text>
    </g>
  </svg>

  <!-- Front header: logo -->
  <svg class="wrap-view wrap-view--front-logo" viewBox="0 0 340 420" aria-label="Front cab header with brand">
    <rect class="panel-white" x="20" y="20" width="300" height="110" rx="10"/>
    <circle class="brand-dot" cx="52" cy="98" r="9"/>
    <text class="brand-name" x="40" y="78" font-size="44" textLength="250" lengthAdjust="spacingAndGlyphs">Quillford</text>
    <text class="brand-tagline" x="300" y="98" font-size="12" text-anchor="end">PLUMBING HEATING</text>
    <text class="brand-tagline" x="300" y="113" font-size="12" text-anchor="end">&amp; AIR CONDITIONING</text>
  </svg>

  <!-- Front header: contact + hood band -->
  <svg class="wrap-view wrap-view--front-contact" viewBox="0 0 340 420" aria-label="Front cab header with contact details and hood band">
    <rect class="panel-white" x="20" y="20" width="300" height="110" rx="10"/>
    <text class="phone" x="170" y="72" font-size="26" text-anchor="middle">(555) 014-7720</text>
    <text class="website" x="170" y="96" font-size="12" text-anchor="middle">www.quillfordpipeworks.example</text>

    <rect class="panel-blue" x="40" y="220" width="260" height="70" rx="8"/>
    <rect class="panel-white" x="54" y="232" width="232" height="46" rx="4"/>
    <circle class="brand-dot" cx="72" cy="255" r="7"/>
    <text class="brand-name" x="88" y="264" font-size="26" textLength="184" lengthAdjust="spacingAndGlyphs">Quillford</text>
  </svg>

  <!-- Rear doors -->
  <svg class="wrap-view wrap-view--rear" viewBox="0 0 340 420" aria-label="Rear door wrap">
    <rect class="panel-white" x="20" y="20" width="300" height="380" rx="6"/>
    <path class="swoosh" d="M20 212 Q170 236 320 200 L320 210 Q170 250 20 222 Z"/>
    <path class="panel-blue" d="M20 222 Q170 250 320 210 L320 394 Q320 400 314 400 L26 400 Q20 400 20 394 Z"/>

    <circle class="brand-dot" cx="50" cy="112" r="10"/>
    <text class="brand-name" x="34" y="88" font-size="52" textLength="270" lengthAdjust="spacingAndGlyphs">Quillford</text>
    <text class="brand-tagline" x="304" y="110" font-size="13" text-anchor="end">PLUMBING HEATING</text>
    <text class="brand-tagline" x="304" y="127" font-size="13" text-anchor="end">&amp; AIR CONDITIONING</text>

    <text class="phone" x="170" y="165" font-size="22" text-anchor="middle">(555) 014-7720</text>
    <text class="website" x="170" y="184" font-size="11" text-anchor="middle">www.quillfordpipeworks.example</text>

    <text class="service-line" x="34" y="268" font-size="7" textLength="272" lengthAdjust="spacingAndGlyphs">RESIDENTIAL AIR CONDITIONING • RESIDENTIAL HEATING • INDOOR AIR QUALITY • RESIDENTIAL PLUMBING</text>
    <text class="service-line" x="40" y="281" font-size="7" textLength="260" lengthAdjust="spacingAndGlyphs">COMMERCIAL AIR CONDITIONING • COMMERCIAL HEATING • COMMERCIAL PLUMBING • GARAGE HEATERS</text>
  </svg>

</main>
</body>
</html>
```